MaxiPlano
Stationery / Business Cards
Professional
Ramiro Quesada
Engineering
Ave. Cerezos 284
San Isidro
Torreon, Coah.
MEXICO
01-800-MaxiPlano
ramiro.quesada@maxiplano.mx
www.maxiplano.mx

```html
<!DOCTYPE html>
<html lang="es">
<head>
<meta charset="utf-8">
<title>MaxiPlano Stationery</title>
<link href="https://fonts.googleapis.com/css2?family=Quicksand:wght@500;700&display=swap" rel="stylesheet">
<style>
:root{
  --backdrop:#2f2f31;
  --paper:#ffffff;
  --paper-shade:#e9ecee;
  --ink:#5a5d60;
  --ink-soft:#8a8e92;
  --sky:#1b8fd2;
  --leaf:#7cc242;
  --sun:#f4c300;
}
*{margin:0;padding:0;box-sizing:border-box}
html,body{width:1200px;height:338px;overflow:hidden;background:var(--backdrop)}
body{position:relative;font-family:"Quicksand",sans-serif;color:var(--ink)}
.sheet{position:absolute;background:var(--paper);box-shadow:0 2px 6px rgba(0,0,0,.45);overflow:hidden}
.sheet svg.band{position:absolute;inset:0;width:100%;height:100%}
.wordmark{font-weight:700;color:var(--ink);white-space:nowrap;position:relative}
.tiny{font-size:4px;line-height:1.5;color:var(--ink-soft);font-weight:500}

.card-front{left:29px;top:19px;width:110px;height:62px;padding:18px 10px}
.card-front .wordmark{font-size:15px}
.card-front .tagline{font-size:5px;color:var(--leaf);margin:4px 0 0 2px}

.card-info{left:34px;top:115px;width:100px;height:50px;padding:8px}
.card-info .name{font-size:6px;font-weight:700;color:var(--sky)}
.card-info .role{font-size:4.5px;color:var(--leaf);margin-bottom:5px}

.card-back{left:34px;top:185px;width:100px;height:60px;display:flex;align-items:center;justify-content:center}
.card-back .wordmark{font-size:11px}
.card-back .strip{position:absolute;left:0;right:0;bottom:0;height:5px;background:var(--sky)}

.letter{top:17px;width:235px;height:315px;padding:18px 20px}
.letter .wordmark{font-size:11px}
.letter .footer{position:absolute;left:20px;right:50px;bottom:12px;text-align:center}
.letter-a{left:150px}
.letter-b{left:395px}

.envelope{left:695px;width:205px;padding:12px 14px}
.envelope .wordmark{font-size:10px}
.envelope .to{position:absolute;left:70px;bottom:24px}
.envelope-a{top:43px;height:125px}
.envelope-b{top:178px;height:120px}

.env-back{left:917px;width:262px;height:90px;background:var(--paper-shade)}
.env-back svg{position:absolute;inset:0;width:100%;height:100%}
.env-back .site{position:absolute;left:0;right:0;top:10px;text-align:center;font-size:5px;letter-spacing:1px;color:var(--paper);font-weight:700}
.env-back-yellow .site{color:var(--ink)}
.env-back-sky{top:20px}
.env-back-yellow{top:108px}
.env-back-white{top:196px;height:110px}
.env-back-white .site{color:var(--sky)}
</style>
</head>
<body>

<div class="sheet card-front">
  <div class="wordmark">MaxiPlano</div>
  <div class="tagline">Engineering Solutions</div>
</div>

<div class="sheet card-info">
  <div class="name">Ramiro Quesada</div>
  <div class="role">Engineering</div>
  <div class="tiny">Ave. Cerezos 284, San Isidro<br>Torreon, Coah. MEXICO<br>01-800-MaxiPlano<br>ramiro.quesada@maxiplano.mx</div>
</div>

<div class="sheet card-back">
  <div class="wordmark">MaxiPlano</div>
  <div class="strip"></div>
</div>

<div class="sheet letter letter-a">
  <svg class="band" viewBox="0 0 235 315" preserveAspectRatio="none" aria-hidden="true">
    <path d="M200,0 C180,110 220,210 195,315 L235,315 L235,0Z" fill="var(--sky)"/>
    <path d="M192,0 C172,110 212,210 187,315" fill="none" stroke="var(--leaf)" stroke-width="3"/>
    <path d="M185,0 C165,110 205,210 180,315" fill="none" stroke="var(--sun)" stroke-width="2"/>
  </svg>
  <div class="wordmark">MaxiPlano</div>
  <div class="tiny footer">Ave. Cerezos 284 · San Isidro · Torreon, Coah. · MEXICO<br>01-800-MaxiPlano · www.maxiplano.mx</div>
</div>

<div class="sheet letter letter-b">
  <svg class="band" viewBox="0 0 235 315" preserveAspectRatio="none" aria-hidden="true">
    <path d="M200,0 C180,110 220,210 195,315 L235,315 L235,0Z" fill="var(--sky)"/>
    <path d="M192,0 C172,110 212,210 187,315" fill="none" stroke="var(--leaf)" stroke-width="3"/>
    <path d="M185,0 C165,110 205,210 180,315" fill="none" stroke="var(--sun)" stroke-width="2"/>
  </svg>
  <div class="wordmark">MaxiPlano</div>
  <div class="tiny footer">Ave. Cerezos 284 · San Isidro · Torreon, Coah. · MEXICO<br>01-800-MaxiPlano · www.maxiplano.mx</div>
</div>

<div class="sheet envelope envelope-a">
  <svg class="band" viewBox="0 0 205 125" preserveAspectRatio="none" aria-hidden="true">
    <path d="M180,0 C165,45 195,85 178,125 L205,125 L205,0Z" fill="var(--sky)"/>
    <path d="M173,0 C158,45 188,85 171,125" fill="none" stroke="var(--leaf)" stroke-width="2"/>
    <path d="M167,0 C152,45 182,85 165,125" fill="none" stroke="var(--sun)" stroke-width="1.5"/>
  </svg>
  <div class="wordmark">MaxiPlano</div>
  <div class="tiny to">Ave. Cerezos 284, San Isidro</div>
</div>

<div class="sheet envelope envelope-b">
  <div class="wordmark">MaxiPlano</div>
  <div class="tiny to">Torreon, Coah. MEXICO</div>
</div>

<div class="sheet env-back env-back-sky">
  <svg viewBox="0 0 262 90" preserveAspectRatio="none" aria-hidden="true">
    <path d="M0,0 L262,0 L262,22 L131,60 L0,22Z" fill="var(--sky)"/>
  </svg>
  <div class="site">www.maxiplano.mx</div>
</div>

<div class="sheet env-back env-back-yellow">
  <svg viewBox="0 0 262 90" preserveAspectRatio="none" aria-hidden="true">
    <path d="M0,0 L262,0 L262,22 L131,60 L0,22Z" fill="var(--sun)"/>
  </svg>
  <div class="site">www.maxiplano.mx</div>
</div>

<div class="sheet env-back env-back-white">
  <svg viewBox="0 0 262 110" preserveAspectRatio="none" aria-hidden="true">
    <path d="M0,0 L262,0 L262,22 L131,60 L0,22Z" fill="var(--paper)" stroke="#cfd4d8" stroke-width="1"/>
  </svg>
  <div class="site">www.maxiplano.mx</div>
</div>

</body>
</html>
```